Business cards for education company

We need a business card design for a relatively new company based in Queensland and operating across Australia. We resell diploma level education courses which include Business, Management, Finance, Community Services & Government courses. We offer over 20 different courses.
The target market is for anyone 16 years of age and older. There is no age limit.

We would like to see the design use the color blue and silver. The final design should communicate professionalism and a bright future.

We sell education but are also promoting the career they see themselves in 2-3 years in the future

Our company logo is attached.

Target Market(s)

We target all age groups above 16 years of age. The main target market would be people aged between 17-35.

We focus on those people who cannot make it into University or do not want to commit the time to a full degree.

Industry/Entity Type

Education

Requirements
Must have
• Professional
Company logo
website
Contact details:

Please use the following example:

Lionel Parfitt
Senior Education Consultant
0417 386 591
Lionel.parfitt@brightwaylearninghub.com.au
www.brightwaylearninghub.com.au

```html
<!DOCTYPE html>
<html lang="en">
<head>
<meta charset="utf-8">
<title>Brightway Learning Hub – Business Card</title>
<link href="https://fonts.googleapis.com/css2?family=Source+Sans+3:wght@400;600;700&display=swap" rel="stylesheet">
<style>
  :root {
    --page-light: #f4f5f6;
    --page-dark: #d8d9db;
    --card-edge: #6c7480;
    --silver-light: #f7f7f5;
    --silver-mid: #d6d7d8;
    --silver-dark: #bfc0c2;
    --blue-light: #b3d3f0;
    --blue-mid: #7eaee0;
    --blue-deep: #4a86c8;
    --blue-shade: #3f78bb;
    --gold-light: #f6e6a8;
    --gold-mid: #c8a968;
    --gold-dark: #7d6232;
    --brand-navy: #1f4e8f;
    --brand-blue: #2f7cc4;
    --name-white: #ffffff;
    --title-cream: #f3e9a9;
    --icon-red: #c0272d;
  }
  html, body {
    margin: 0;
    width: 1200px;
    height: 1200px;
    overflow: hidden;
  }
  body {
    background: radial-gradient(ellipse at 50% 40%, var(--page-light) 0%, var(--page-dark) 100%);
    font-family: "Source Sans 3", "Myriad Pro", Arial, sans-serif;
  }
  .business-card {
    position: absolute;
    left: 110px;
    top: 302px;
    width: 982px;
    height: 593px;
    display: block;
    outline: 1px solid var(--card-edge);
  }
  .brand-name { font-weight: 700; fill: var(--brand-navy); letter-spacing: 1px; }
  .holder-name { font-weight: 700; fill: var(--name-white); font-size: 19px; letter-spacing: 0.5px; }
  .holder-title { font-weight: 400; fill: var(--title-cream); font-size: 17.5px; }
  .contact-line { font-weight: 400; fill: var(--name-white); font-size: 18px; }
</style>
</head>
<body>
<svg class="business-card" viewBox="0 0 818 494" xmlns="http://www.w3.org/2000/svg" aria-label="Brightway Learning Hub business card for Lionel Parfitt">
  <defs>
    <linearGradient id="silverFace" x1="0" y1="0" x2="0" y2="1">
      <stop offset="0" stop-color="var(--silver-mid)"/>
      <stop offset="0.5" stop-color="var(--silver-light)"/>
      <stop offset="1" stop-color="var(--silver-dark)"/>
    </linearGradient>
    <radialGradient id="logoGlow" cx="0.5" cy="0.5" r="0.55">
      <stop offset="0" stop-color="#ffffff"/>
      <stop offset="0.7" stop-color="#f2f2f0"/>
      <stop offset="1" stop-color="#e4e4e3" stop-opacity="0"/>
    </radialGradient>
    <radialGradient id="blueFace" cx="0.52" cy="0.55" r="0.6">
      <stop offset="0" stop-color="var(--blue-light)"/>
      <stop offset="0.55" stop-color="var(--blue-mid)"/>
      <stop offset="1" stop-color="var(--blue-deep)"/>
    </radialGradient>
    <linearGradient id="goldBand" x1="0" y1="0" x2="1" y2="0">
      <stop offset="0" stop-color="var(--gold-dark)"/>
      <stop offset="0.18" stop-color="var(--gold-light)"/>
      <stop offset="0.35" stop-color="var(--gold-mid)"/>
      <stop offset="0.55" stop-color="var(--gold-light)"/>
      <stop offset="0.75" stop-color="var(--gold-dark)"/>
      <stop offset="0.9" stop-color="var(--gold-light)"/>
      <stop offset="1" stop-color="var(--gold-mid)"/>
    </linearGradient>
  </defs>

  <!-- silver upper face -->
  <rect class="silver-face" x="0" y="0" width="818" height="494" fill="url(#silverFace)"/>
  <rect class="logo-strip" x="110" y="25" width="610" height="138" fill="url(#logoGlow)"/>

  <!-- brand -->
  <g class="brand">
    <circle cx="282" cy="96" r="34" fill="var(--brand-blue)"/>
    <text class="brand-name" x="334" y="96" font-size="34">BRIGHTWAY</text>
    <text class="brand-name" x="336" y="122" font-size="18" letter-spacing="3">LEARNING HUB</text>
  </g>

  <!-- blue lower face with wave -->
  <path class="wave-shadow" d="M0,288 C150,322 250,302 400,288 C550,274 650,302 818,282 L818,494 L0,494 Z" fill="var(--blue-shade)"/>
  <path class="blue-face" d="M0,292 C150,326 250,306 400,292 C550,278 650,306 818,286 L818,494 L0,494 Z" fill="url(#blueFace)"/>
  <path class="gold-band" d="M0,270 C150,304 250,284 400,270 C550,256 650,286 818,264" fill="none" stroke="url(#goldBand)" stroke-width="16"/>

  <!-- card holder -->
  <text class="holder-name" x="46" y="356">LIONEL PARFITT</text>
  <text class="holder-title" x="46" y="381">Senior Education Consultant</text>

  <!-- contact details -->
  <g class="contact-phone">
    <circle cx="337" cy="405" r="8.5" fill="var(--icon-red)"/>
    <path d="M333,401 q1,-2 2.5,-1 l1,2.5 -1.5,1 q1,2.5 3,3.5 l1,-1.5 2.5,1 q1,1.5 -1,2.5 q-5,0 -7.5,-8 z" fill="#fff"/>
    <text class="contact-line" x="354" y="412">0417 386 591</text>
  </g>
  <g class="contact-email">
    <circle cx="337" cy="430" r="8.5" fill="var(--icon-red)"/>
    <rect x="331.5" y="426" width="11" height="8" fill="#fff"/>
    <path d="M331.5,426 L337,431 L342.5,426" fill="none" stroke="var(--icon-red)" stroke-width="1.2"/>
    <text class="contact-line" x="354" y="437">Lionel.parfitt@brightwaylearninghub.com.au</text>
  </g>
  <g class="contact-web">
    <circle cx="337" cy="454" r="8.5" fill="var(--icon-red)"/>
    <g fill="none" stroke="#fff" stroke-width="1">
      <circle cx="337" cy="454" r="5.5"/>
      <ellipse cx="337" cy="454" rx="2.5" ry="5.5"/>
      <line x1="331.5" y1="454" x2="342.5" y2="454"/>
    </g>
    <text class="contact-line" x="354" y="461">www.brightwaylearninghub.com.au</text>
  </g>
</svg>
</body>
</html>
```